VornaDesk website (https://vornadesk.example) re-design

Website purposed for providing general information on products we develop and offer. Products are software specific to online poker players.
Software not playful but complex technological solutions so website should look neatly and professional.
More details on the project you may find in this document:
https://papers.quillnest.example/doc/7TmR2kZpW9xLqB4nVc8YdHs3EfGaJu6KoPi1NwXe/edit#section=s.qkmz4f81b2rn
Or below:
Technology: preferable bootstrap, but not critical
CrossPlatform: Desktop/Mobile
Pages:
Main (Current https://vornadesk.example/)
Video, Room list, Features, Price, Contacts
Partner section (whom we work with)
Documentation and FAQ links
Login (Current https://vornadesk.example/Login/Login)
SignUp/Password recovery (https://vornadesk.example/Signup/Signup, https://vornadesk.example/Login/RemindPassword)
License token (unique and assigned per customer). Need an option to copy to clipboard from Dashboard screen.
Download link for latest product version.
Subs end date to display
Manuals FAQ links
Buy and renew subscription
Notes: Group everything related to subscription into one logic block on the screen.
FAQ (https://vornadesk.example/Home/FAQ).
Simple and comfortable in usage faq.
Notes: Combine all the steps into one screen.
Make download trial which leads to registration!
Target Market(s)
Online poker players
Number of Pages Required
5+ page

```html
<!DOCTYPE html>
<html lang="en">
<head>
<meta charset="utf-8">
<title>VornaDesk — Online Poker Software</title>
<link rel="stylesheet" href="https://fonts.googleapis.com/css2?family=Roboto:wght@400;500;700;900&family=Open+Sans:wght@400;600;700&display=swap">
<style>
:root{
  --orange:#f5821f;
  --blue:#1b9be6;
  --navy:#1d2a4d;
  --ink:#2b2b2b;
  --muted:#555;
  --soft:#f3f1f2;
  --line:#d9d9d9;
  --dark:#1c2132;
  --light-blue:#eef6fc;
}
*{box-sizing:border-box;margin:0;padding:0}
html,body{width:1200px;height:4471px;overflow:hidden}
body{font-family:"Open Sans",Arial,sans-serif;color:var(--ink);background:#fff;font-size:14px}
.section-title{font-family:"Roboto",Arial,sans-serif;font-weight:700;font-size:27px;letter-spacing:.5px;text-align:center;color:#1a1a1a}
.section-title::after{content:"";display:block;width:42px;height:3px;background:#b5b5b5;margin:16px auto 0}

/* header */
.site-header{height:72px;display:flex;align-items:center;padding:0 132px;background:#fff}
.brand{font-family:"Roboto",Arial,sans-serif;font-weight:700;font-size:27px;color:#222}
.main-nav{margin-left:auto;display:flex;align-items:center;gap:6px;margin-right:-66px}
.main-nav a{font-family:"Roboto",Arial,sans-serif;font-weight:500;font-size:13px;color:#222;text-decoration:none;padding:5px 7px;text-transform:uppercase;margin-left:6px}
.main-nav a.active{background:var(--orange);color:#fff}
.main-nav a.login{border:2px solid var(--orange);color:var(--orange);padding:4px 10px;margin-left:18px}

/* hero */
.hero{height:558px;position:relative;background:radial-gradient(ellipse at 80% 40%,#4a2a38 0%,#241d2c 35%,#15161f 75%);text-align:center;color:#fff;overflow:hidden}
.hero h1{font-family:"Roboto",Arial,sans-serif;font-weight:700;font-size:35px;padding-top:60px;letter-spacing:1px}
.hero p{font-family:"Roboto",Arial,sans-serif;font-size:18px;margin-top:10px;letter-spacing:.3px}
.hero-art{position:absolute;left:40px;top:70px;width:220px;height:230px;border-radius:14px;background:linear-gradient(140deg,#2c2a30,#17171c);opacity:.7}
.hero-chips{position:absolute;right:20px;top:40px;width:360px;height:420px;border-radius:50%;background:radial-gradient(circle,#5a2c3a 0%,#2a1d28 55%,transparent 72%)}
.hero-video{position:absolute;left:340px;top:180px;width:527px;height:340px;background:linear-gradient(90deg,#3b3c42 0 25%,#4a4b52 25% 100%)}

/* features */
.features{height:843px;background:var(--soft);padding-top:68px}
.feature-grid{width:938px;margin:49px auto 0;display:grid;grid-template-columns:repeat(3,298px);gap:24px 22px}
.feature-card{background:#fff;height:296px;box-shadow:0 2px 6px rgba(0,0,0,.08);text-align:center;padding:38px 30px 0}
.feature-icon{width:68px;height:68px;border-radius:50%;background:var(--blue);margin:0 auto;display:flex;align-items:center;justify-content:center}
.feature-card h3{font-family:"Roboto",Arial,sans-serif;font-weight:500;font-size:16px;margin-top:26px;color:#111}
.feature-card p{font-size:14px;line-height:19px;color:#333;margin-top:14px}

/* pricing */
.pricing{height:756px;background:#fff;padding-top:44px}
.plan-row{display:flex;justify-content:center;align-items:flex-start;gap:34px;margin-top:42px}
.plan{width:265px;background:#fff;box-shadow:0 2px 10px rgba(0,0,0,.1);text-align:center;padding:28px 0 30px}
.plan h3{font-family:"Roboto",Arial,sans-serif;font-weight:700;font-size:18px;color:var(--navy)}
.plan-art{width:100px;height:96px;margin:18px auto 0;border-radius:8px;background:linear-gradient(135deg,#dff0fb,#b9dcf3)}
.plan .from{font-size:11px;color:#444;margin-top:20px}
.plan .price{font-family:"Roboto",Arial,sans-serif;font-weight:700;font-size:35px;color:var(--navy);line-height:40px}
.plan .per{font-size:11px;color:#444}
.plan ul{list-style:none;text-align:left;padding-left:28px;margin-top:20px}
.plan li{font-size:13px;color:#333;line-height:25px;display:flex;align-items:center;gap:8px}
.tick{width:10px;height:8px}
.btn{display:inline-block;background:var(--orange);color:#fff;font-family:"Roboto",Arial,sans-serif;font-weight:700;font-size:12px;padding:7px 14px;border-radius:4px;text-decoration:none;margin-top:18px}

/* documentation */
.docs{height:559px;background:#ededee;padding:50px 0 0 130px;position:relative}
.docs h2{font-family:"Roboto",Arial,sans-serif;font-weight:700;font-size:28px;color:#1a1a1a}
.docs h2::after{content:"";display:block;width:42px;height:3px;background:#b5b5b5;margin-top:14px}
.doc-shot{position:absolute;left:130px;top:107px;width:535px;height:396px;background:linear-gradient(#e9eaec 0 30px,#1e1f22 30px 66px,#fff 66px);box-shadow:0 2px 8px rgba(0,0,0,.08)}
.doc-card{position:absolute;left:665px;top:111px;width:403px;height:405px;background:#fff;box-shadow:0 2px 10px rgba(0,0,0,.1);padding:14px}
.doc-card-inner{border:1px solid #ccc;height:100%;padding:50px 32px 0}
.doc-card h3{font-family:"Roboto",Arial,sans-serif;font-weight:500;font-size:16px;line-height:22px;color:#111}
.doc-card p{font-size:15px;line-height:22px;color:#333;margin-top:20px}
.doc-card .btn{font-size:14px;padding:9px 18px;margin-top:24px}

/* faq */
.faq{height:695px;background:#fff;padding-top:48px}
.faq-list{width:848px;margin:40px auto 0;border:1px solid var(--line)}
.faq-item{height:54px;border-bottom:1px solid var(--line);display:flex;align-items:center;justify-content:space-between;padding:0 22px;font-size:15px;color:#333}
.faq-item:last-child{border-bottom:none}
.faq-item.open{background:var(--blue);color:#fff;font-weight:600;border-bottom:none}
.faq-answer{background:var(--light-blue);padding:18px 22px;font-size:14px;line-height:17px;color:#333;border-bottom:1px solid var(--line)}
.faq-answer p+p{margin-top:16px}
.chev{width:12px;height:8px}

/* contact */
.contact{height:500px;background:var(--dark);padding-top:50px}
.contact .section-title{color:#fff}
.contact .section-title::after{display:none}
.contact-form{width:638px;margin:44px auto 0;display:grid;grid-template-columns:310px 310px;gap:14px 18px}
.field{height:45px;background:#fff;padding:14px 18px;font-family:"Roboto",Arial,sans-serif;font-weight:500;font-size:13px;color:#222}
.field.message{grid-column:1/3;height:110px}
.submit{grid-column:1/3;justify-self:center;background:var(--orange);color:#fff;font-family:"Roboto",Arial,sans-serif;font-weight:700;font-size:17px;padding:9px 20px;border-radius:5px;margin-top:20px}

/* partners */
.partners{height:316px;background:#fff;padding-top:56px;position:relative}
.partner-row{width:940px;margin:46px auto 0;display:flex;justify-content:space-between}
.partner{width:84px;height:84px;border-radius:10px}
.slide-arrow{position:absolute;top:188px;width:14px;height:26px}
.slide-arrow.prev{left:64px}
.slide-arrow.next{right:64px}

/* footer */
.site-footer{height:172px;background:#f4f3f5;padding:34px 132px 0}
.footer-top{display:flex;align-items:center}
.footer-top .brand{font-size:27px}
.footer-nav{margin-left:auto;display:flex;gap:22px}
.footer-nav a{font-family:"Roboto",Arial,sans-serif;font-size:12px;color:#222;text-decoration:none;text-transform:uppercase}
.footer-rule{display:flex;align-items:center;margin-top:20px}
.footer-rule hr{flex:1;border:none;border-top:1px solid #bbb}
.social{display:flex;gap:8px;margin-left:14px}
.social span{width:26px;height:26px;border-radius:50%;background:#1f5fc4}
.social span:nth-child(2){background:#1a95e0}
.social span:nth-child(3){background:#133e8a}
.copyright{text-align:center;font-size:11px;color:#333;margin-top:8px}
</style>
</head>
<body>

<header class="site-header">
  <div class="brand">VornaDesk</div>
  <nav class="main-nav">
    <a class="active" href="#">Home</a>
    <a href="#">About us</a>
    <a href="#">Room list</a>
    <a href="#">Features</a>
    <a href="#">Price</a>
    <a href="#">FAQ</a>
    <a href="#">Contact us</a>
    <a class="login" href="#">Login</a>
  </nav>
</header>

<section class="hero">
  <div class="hero-art" role="img" aria-label="Playing cards decoration"></div>
  <div class="hero-chips" role="img" aria-label="Poker chips decoration"></div>
  <h1>ONLINE POKER</h1>
  <p>LOREM IPSUM IS SIMPLY DUMMY TEXT OF THE</p>
  <div class="hero-video" role="img" aria-label="Product video showing the software settings screen with the poker room list"></div>
</section>

<section class="features">
  <h2 class="section-title">FEATURES</h2>
  <div class="feature-grid">
    <div class="feature-card">
      <div class="feature-icon"><svg width="34" height="34" viewBox="0 0 24 24" fill="none" stroke="#fff" stroke-width="2"><path d="M12 2l8 3v6c0 5-3.5 9-8 11-4.5-2-8-6-8-11V5z"/><path d="M8 12l3 3 5-6"/></svg></div>
      <h3>LOREM IPSUM</h3>
      <p>Lorem ipsum dolor sit amet, consectetur adipiscing elit, sed do eiusmod tempor incididunt ut labore et dolore magn.</p>
    </div>
    <div class="feature-card">
      <div class="feature-icon"><svg width="34" height="34" viewBox="0 0 24 24" fill="#fff"><rect x="4" y="14" width="3" height="6"/><rect x="9" y="10" width="3" height="10"/><rect x="14" y="7" width="3" height="13"/><rect x="19" y="4" width="2" height="16"/></svg></div>
      <h3>LOREM IPSUM</h3>
      <p>Lorem ipsum dolor sit amet, consectetur adipiscing elit, sed do eiusmod tempor incididunt ut labore et dolore magn.</p>
    </div>
    <div class="feature-card">
      <div class="feature-icon"><svg width="34" height="34" viewBox="0 0 24 24" fill="#fff"><path d="M12 2l10 5H2z"/><rect x="4" y="9" width="2.5" height="9"/><rect x="8.5" y="9" width="2.5" height="9"/><rect x="13" y="9" width="2.5" height="9"/><rect x="17.5" y="9" width="2.5" height="9"/><rect x="2" y="19" width="20" height="3"/></svg></div>
      <h3>LOREM IPSUM</h3>
      <p>Lorem ipsum dolor sit amet, consectetur adipiscing elit, sed do eiusmod tempor incididunt ut labore et dolore magn.</p>
    </div>
    <div class="feature-card">
      <div class="feature-icon"><svg width="34" height="34" viewBox="0 0 24 24" fill="none" stroke="#fff" stroke-width="2"><rect x="3" y="4" width="16" height="16" rx="2"/><path d="M9 15l1-4 8-8 3 3-8 8z"/></svg></div>
      <h3>LOREM IPSUM</h3>
      <p>Lorem ipsum dolor sit amet, consectetur adipiscing elit, sed do eiusmod tempor incididunt ut labore et dolore magn.</p>
    </div>
    <div class="feature-card">
      <div class="feature-icon"><svg width="34" height="34" viewBox="0 0 24 24" fill="none" stroke="#fff" stroke-width="2.2"><circle cx="9" cy="14" r="4"/><circle cx="17" cy="7" r="3"/><path d="M9 7v2M9 19v2M2 14h2M14 14h2M17 2v1.5M17 10.5V12M12 7h1.5M20.5 7H22"/></svg></div>
      <h3>LOREM IPSUM</h3>
      <p>Lorem ipsum dolor sit amet, consectetur adipiscing elit, sed do eiusmod tempor incididunt ut labore et dolore magn.</p>
    </div>
    <div class="feature-card">
      <div class="feature-icon"><svg width="34" height="34" viewBox="0 0 24 24" fill="none" stroke="#fff" stroke-width="2"><rect x="3" y="5" width="18" height="14" rx="2"/><path d="M7 9h2v2H7zM11 9h2v2h-2zM15 9h2v2h-2zM7 13h2v2H7zM11 13h2v2h-2zM15 13h2v2h-2z"/></svg></div>
      <h3>LOREM IPSUM</h3>
      <p>Lorem ipsum dolor sit amet, consectetur adipiscing elit, sed do eiusmod tempor incididunt ut labore et dolore magn.</p>
    </div>
  </div>
</section>

<section class="pricing">
  <h2 class="section-title">PRICING</h2>
  <div class="plan-row">
    <div class="plan">
      <h3>Support</h3>
      <div class="plan-art" role="img" aria-label="Illustration of a hand holding a card with a chip"></div>
      <div class="from">Starting at</div>
      <div class="price">$30</div>
      <div class="per">per month</div>
      <ul>
        <li><svg class="tick" viewBox="0 0 10 8"><path d="M1 4l3 3 5-6" fill="none" stroke="#1b9be6" stroke-width="2"/></svg>Lorem ipsum dolor sit amet</li>
        <li><svg class="tick" viewBox="0 0 10 8"><path d="M1 4l3 3 5-6" fill="none" stroke="#1b9be6" stroke-width="2"/></svg>Consectetur adipiscing</li>
        <li><svg class="tick" viewBox="0 0 10 8"><path d="M1 4l3 3 5-6" fill="none" stroke="#1b9be6" stroke-width="2"/></svg>Nemo enim ipsam</li>
        <li><svg class="tick" viewBox="0 0 10 8"><path d="M1 4l3 3 5-6" fill="none" stroke="#1b9be6" stroke-width="2"/></svg>Nam libero tempore</li>
        <li><svg class="tick" viewBox="0 0 10 8"><path d="M1 4l3 3 5-6" fill="none" stroke="#1b9be6" stroke-width="2"/></svg>when our power of choice</li>
      </ul>
      <a class="btn" href="#">Get Started</a>
    </div>
    <div class="plan">
      <h3>Basic</h3>
      <div class="plan-art" role="img" aria-label="Illustration of a person working at a desk computer"></div>
      <div class="from">Starting at</div>
      <div class="price">$60</div>
      <div class="per">per month</div>
      <ul>
        <li><svg class="tick" viewBox="0 0 10 8"><path d="M1 4l3 3 5-6" fill="none" stroke="#1b9be6" stroke-width="2"/></svg>Lorem ipsum dolor sit amet</li>
        <li><svg class="tick" viewBox="0 0 10 8"><path d="M1 4l3 3 5-6" fill="none" stroke="#1b9be6" stroke-width="2"/></svg>Consectetur adipiscing</li>
        <li><svg class="tick" viewBox="0 0 10 8"><path d="M1 4l3 3 5-6" fill="none" stroke="#1b9be6" stroke-width="2"/></svg>Nemo enim ipsam</li>
        <li><svg class="tick" viewBox="0 0 10 8"><path d="M1 4l3 3 5-6" fill="none" stroke="#1b9be6" stroke-width="2"/></svg>Nam libero tempore</li>
        <li><svg class="tick" viewBox="0 0 10 8"><path d="M1 4l3 3 5-6" fill="none" stroke="#1b9be6" stroke-width="2"/></svg>when our power of choice</li>
        <li><svg class="tick" viewBox="0 0 10 8"><path d="M1 4l3 3 5-6" fill="none" stroke="#1b9be6" stroke-width="2"/></svg>Lorem ipsum dolor sit amet</li>
      </ul>
      <a class="btn" href="#">Get Started</a>
    </div>
    <div class="plan">
      <h3>Premium</h3>
      <div class="plan-art" role="img" aria-label="Illustration of a computer workstation with charts"></div>
      <div class="from">Starting at</div>
      <div class="price">$75</div>
      <div class="per">per month</div>
      <ul>
        <li><svg class="tick" viewBox="0 0 10 8"><path d="M1 4l3 3 5-6" fill="none" stroke="#1b9be6" stroke-width="2"/></svg>Lorem ipsum dolor sit amet</li>
        <li><svg class="tick" viewBox="0 0 10 8"><path d="M1 4l3 3 5-6" fill="none" stroke="#1b9be6" stroke-width="2"/></svg>Consectetur adipiscing</li>
        <li><svg class="tick" viewBox="0 0 10 8"><path d="M1 4l3 3 5-6" fill="none" stroke="#1b9be6" stroke-width="2"/></svg>Nemo enim ipsam</li>
        <li><svg class="tick" viewBox="0 0 10 8"><path d="M1 4l3 3 5-6" fill="none" stroke="#1b9be6" stroke-width="2"/></svg>Nam libero tempore</li>
        <li><svg class="tick" viewBox="0 0 10 8"><path d="M1 4l3 3 5-6" fill="none" stroke="#1b9be6" stroke-width="2"/></svg>when our power of choice</li>
        <li><svg class="tick" viewBox="0 0 10 8"><path d="M1 4l3 3 5-6" fill="none" stroke="#1b9be6" stroke-width="2"/></svg>Lorem ipsum dolor sit amet</li>
        <li><svg class="tick" viewBox="0 0 10 8"><path d="M1 4l3 3 5-6" fill="none" stroke="#1b9be6" stroke-width="2"/></svg>Consectetur adipiscing</li>
        <li><svg class="tick" viewBox="0 0 10 8"><path d="M1 4l3 3 5-6" fill="none" stroke="#1b9be6" stroke-width="2"/></svg>Nemo enim ipsam</li>
      </ul>
      <a class="btn" href="#">Get Started</a>
    </div>
  </div>
</section>

<section class="docs">
  <h2>DOCUMENTATION</h2>
  <div class="doc-shot" role="img" aria-label="Screenshot of the customer dashboard with account info, license token and plan selection"></div>
  <div class="doc-card">
    <div class="doc-card-inner">
      <h3>LOREM IPSUM DOLOR SIT AMET CONSECTETUR ADIPISCI</h3>
      <p>Sed ut perspiciatis unde omnis iste natus error sit voluptatem accusantium dol oremque laudantium, totam rem aperi am, eaque ipsa quae ab illo inven tore veritatis et quasi architecto beatae vitae dicta sunt explicabo.</p>
      <a class="btn" href="#">Read More</a>
    </div>
  </div>
</section>

<section class="faq">
  <h2 class="section-title">FAQ</h2>
  <div class="faq-list">
    <div class="faq-item">Which Rooms does VornaDesk support?<svg class="chev" viewBox="0 0 12 8"><path d="M1 1l5 5 5-5" fill="none" stroke="#333" stroke-width="1.6"/></svg></div>
    <div class="faq-item open">Can't find your room in the list?<svg class="chev" viewBox="0 0 12 8"><path d="M1 7l5-5 5 5" fill="none" stroke="#fff" stroke-width="1.6"/></svg></div>
    <div class="faq-answer">
      <p>Feel free to contact us with corresponding request: help@vornadesk.example</p>
      <p>In your email please refer to the room name/website/download link and any additional information which could be helpful for initial review. We will definitely reply you back.</p>
    </div>
    <div class="faq-item">Does VornaDesk working with VPN?<svg class="chev" viewBox="0 0 12 8"><path d="M1 1l5 5 5-5" fill="none" stroke="#333" stroke-width="1.6"/></svg></div>
    <div class="faq-item">How many tables I may play at the same time with VornaDesk running?<svg class="chev" viewBox="0 0 12 8"><path d="M1 1l5 5 5-5" fill="none" stroke="#333" stroke-width="1.6"/></svg></div>
    <div class="faq-item">Does PlayPoint support 5 card PLO?<svg class="chev" viewBox="0 0 12 8"><path d="M1 1l5 5 5-5" fill="none" stroke="#333" stroke-width="1.6"/></svg></div>
    <div class="faq-item">Do you support ShortDeck play?<svg class="chev" viewBox="0 0 12 8"><path d="M1 1l5 5 5-5" fill="none" stroke="#333" stroke-width="1.6"/></svg></div>
    <div class="faq-item">Does VornaDesk support tourneys?<svg class="chev" viewBox="0 0 12 8"><path d="M1 1l5 5 5-5" fill="none" stroke="#333" stroke-width="1.6"/></svg></div>
  </div>
</section>

<section class="contact">
  <h2 class="section-title">CONTACT US</h2>
  <form class="contact-form">
    <div class="field">NAME</div>
    <div class="field">E MAIL</div>
    <div class="field">PHONE</div>
    <div class="field">SUBJECT</div>
    <div class="field message">MESSAGE</div>
    <div class="submit">Submit</div>
  </form>
</section>

<section class="partners">
  <h2 class="section-title">PARTNER</h2>
  <svg class="slide-arrow prev" viewBox="0 0 14 26"><path d="M12 2L2 13l10 11" fill="none" stroke="#bbb" stroke-width="2"/></svg>
  <div class="partner-row">
    <div class="partner" style="background:#1b1b1d"></div>
    <div class="partner" style="background:#2a2317"></div>
    <div class="partner" style="background:#2bbfa4"></div>
    <div class="partner" style="background:#221a12"></div>
    <div class="partner" style="background:#1e7a4c"></div>
    <div class="partner" style="background:#151515"></div>
    <div class="partner" style="background:#f39324"></div>
  </div>
  <svg class="slide-arrow next" viewBox="0 0 14 26"><path d="M2 2l10 11L2 24" fill="none" stroke="#bbb" stroke-width="2"/></svg>
</section>

<footer class="site-footer">
  <div class="footer-top">
    <div class="brand">VornaDesk</div>
    <nav class="footer-nav">
      <a href="#">Home</a><a href="#">About us</a><a href="#">Room list</a><a href="#">Features</a><a href="#">Price</a><a href="#">FAQ</a><a href="#">Contact us</a>
    </nav>
  </div>
  <div class="footer-rule"><hr><div class="social"><span></span><span></span><span></span></div></div>
  <p class="copyright">Copyright © 2020 All Rights Reserved</p>
</footer>

</body>
</html>
```